Want a package created for a new protein bar

We would like a new package created for a new protein bar project The name of the bar will be VOLMBite a real food protein bar, we would like a ‘window’ on the package of bar like Brave Meadow bar below in images.

VOLMBite
‘Super Food Bar’
14g of Whey Protein
The package film size is the following 12cm width x 15cm Length,
Flavor Peanut Chocolate Chip, additional information will be attached shortly like nutrition facts,

Target Market(s)

fitness market, bodybuilders, athletes, everyday people

Industry/Entity Type

Health Product

Logo Text

VOLMBite

Font styles to use
Serif
Sans Serif
Decorative

Requirements
Must have
• Package window

```html
<!DOCTYPE html>
<html lang="en">
<head>
<meta charset="utf-8">
<title>VOLMBite – Super Food Bar wrapper</title>
<link href="https://fonts.googleapis.com/css2?family=Roboto+Condensed:wght@700;900&display=swap" rel="stylesheet">
<style>
  :root {
    --backdrop: #ecd8bd;
    --wrapper-brown: #4a3233;
    --wrapper-shade: #3f2a2b;
    --label-white: #ffffff;
    --logo-gold: #c38b34;
    --ink-brown: #4a3233;
    --badge-gold: #b98838;
    --badge-cream: #f3dca7;
    --photo-light: #e0b273;
    --photo-dark: #8a5a34;
  }
  * { margin: 0; padding: 0; box-sizing: border-box; }
  html, body {
    width: 1200px; height: 1200px; overflow: hidden;
    background: var(--backdrop);
    font-family: "Roboto Condensed", "Arial Narrow", sans-serif;
  }
  .wrapper {
    position: absolute; left: 90px; top: 440px;
    width: 1020px; height: 300px;
  }
  .wrapper-crimps { position: absolute; inset: 0; }
  .wrapper-body {
    position: absolute; left: 80px; top: 0;
    width: 860px; height: 300px;
    background: var(--wrapper-brown);
    overflow: hidden;
  }
  .label-band {
    position: absolute; left: 0; top: 0;
    width: 620px; height: 120px;
    background: var(--label-white);
  }
  .brand-name {
    position: absolute; left: 26px; top: 14px;
    font-weight: 900; font-size: 92px; line-height: 1;
    color: var(--logo-gold); letter-spacing: 1px;
  }
  .tagline {
    position: absolute; left: 470px; top: 26px;
    font-weight: 700; font-size: 30px; line-height: 0.95;
    color: var(--ink-brown); text-transform: uppercase;
  }
  .flavor {
    position: absolute; left: 26px; top: 138px;
    font-weight: 700; font-size: 34px; color: var(--label-white);
    text-transform: uppercase; letter-spacing: 0.5px;
  }
  .claims {
    position: absolute; left: 26px; top: 188px;
    font-weight: 700; font-size: 16px; color: var(--label-white);
    text-transform: uppercase; word-spacing: 2px;
  }
  .claims span { margin: 0 10px; }
  .protein-badge {
    position: absolute; left: 548px; top: 132px;
    width: 60px; height: 58px;
    background: var(--badge-gold); border-radius: 4px;
    color: var(--label-white); text-align: center;
    font-weight: 700;
  }
  .protein-badge .amount { font-size: 26px; line-height: 34px; display: block; }
  .protein-badge .unit {
    display: block; background: var(--badge-cream); color: var(--ink-brown);
    font-size: 12px; line-height: 20px; margin: 0 4px; border-radius: 2px;
  }
  .product-window {
    position: absolute; left: 640px; top: 0;
    width: 220px; height: 220px;
    background: radial-gradient(circle at 55% 40%, var(--photo-light), var(--photo-dark));
  }
</style>
</head>
<body>
  <div class="wrapper">
    <svg class="wrapper-crimps" width="1020" height="300" viewBox="0 0 1020 300" aria-hidden="true">
      <path fill="var(--wrapper-shade)" d="M0 10 L90 20 L90 280 L0 290
        L8 275 L0 260 L8 245 L0 230 L8 215 L0 200 L8 185 L0 170 L8 155 L0 140
        L8 125 L0 110 L8 95 L0 80 L8 65 L0 50 L8 35 L0 20 Z"/>
      <path fill="var(--wrapper-shade)" d="M1020 10 L930 20 L930 280 L1020 290
        L1012 275 L1020 260 L1012 245 L1020 230 L1012 215 L1020 200 L1012 185 L1020 170 L1012 155 L1020 140
        L1012 125 L1020 110 L1012 95 L1020 80 L1012 65 L1020 50 L1012 35 L1020 20 Z"/>
    </svg>
    <div class="wrapper-body">
      <div class="label-band">
        <div class="brand-name">VOLMBite</div>
        <div class="tagline">Super<br>Food Bar</div>
      </div>
      <div class="flavor">Flavor Peanut Chocolate Chip</div>
      <div class="claims">Lorem Ipsum<span>|</span>Lorem Ipsum<span>|</span>Lorem Ipsum</div>
      <div class="protein-badge"><span class="amount">14g</span><span class="unit">Protein</span></div>
      <div class="product-window" role="img" aria-label="Photo of the peanut chocolate chip protein bar with peanuts and pretzels"></div>
    </div>
  </div>
</body>
</html>
```